north lark upkeep services

Target Market(s)

General letter head for emails and letter quotes ect

Colors
0054AA
0677BA
7BADD7
CADEEF
E8F1F8
0094D4
00A9DD
6FCCEA
C7EBF8
E9F6FB

Requirements
Must have
• logo phone email website names
Nice to have
• what we do (from the website)

```html
<!DOCTYPE html>
<html lang="en">
<head>
<meta charset="utf-8">
<title>North Lark Upkeep Services – Letterhead</title>
<link href="https://fonts.googleapis.com/css2?family=Poppins:wght@600&family=Arimo:wght@400;700&display=swap" rel="stylesheet">
<style>
  :root {
    --navy: #1e2a78;
    --brand: #0054AA;
    --mid-blue: #0677BA;
    --sky: #00A9DD;
    --cyan: #0094D4;
    --ink: #333333;
    --rule: #4a4a4a;
    --paper: #ffffff;
    --backdrop: #e6e6e8;
  }
  * { box-sizing: border-box; margin: 0; padding: 0; }
  html, body { width: 1200px; height: 960px; overflow: hidden; }
  body {
    background: var(--backdrop);
    font-family: "Arimo", Arial, sans-serif;
    color: var(--ink);
    position: relative;
  }
  .letterhead {
    position: absolute;
    left: 282px;
    top: 30px;
    width: 636px;
    height: 900px;
    background: var(--paper);
    box-shadow: 0 6px 24px rgba(0,0,0,.12);
    overflow: hidden;
  }
  .brand {
    position: absolute;
    left: 64px;
    top: 48px;
    display: flex;
    align-items: center;
    gap: 10px;
  }
  .brand-dot {
    width: 34px; height: 34px; border-radius: 50%;
    background: var(--brand);
  }
  .brand-name {
    font-family: "Poppins", sans-serif;
    font-weight: 600;
    font-size: 15px;
    line-height: 1.1;
    color: var(--brand);
    text-transform: uppercase;
    letter-spacing: .02em;
    width: 150px;
  }
  .header-rule {
    position: absolute;
    left: 246px;
    right: 52px;
    top: 104px;
    height: 1px;
    background: var(--rule);
  }
  .contact {
    position: absolute;
    left: 436px;
    top: 34px;
    padding-left: 12px;
    border-left: 1px solid var(--rule);
    height: 70px;
    font-size: 9px;
    line-height: 12px;
    color: var(--ink);
  }
  .contact-line { display: flex; align-items: center; gap: 5px; }
  .contact-line svg { width: 8px; height: 8px; flex: none; }
  .contact-address { margin-bottom: 1px; padding-left: 0; }
  .letter {
    position: absolute;
    left: 92px;
    right: 70px;
    top: 230px;
  }
  .salutation {
    font-family: "Poppins", sans-serif;
    font-weight: 600;
    font-size: 14px;
    color: #3a3a3a;
    margin-bottom: 12px;
  }
  .letter p {
    font-size: 10.5px;
    line-height: 14.5px;
    margin-bottom: 14px;
    margin-left: 26px;
  }
  .closing {
    margin-top: 20px;
    margin-left: 60px;
    font-size: 9.5px;
    font-weight: 700;
  }
  .signature {
    display: block;
    margin: 14px 0 0 80px;
    width: 130px;
    height: 34px;
    border-radius: 3px;
    background: linear-gradient(90deg, #ececec, #f6f6f6);
  }
  .footer-band {
    position: absolute;
    left: 0; bottom: 0;
    width: 636px; height: 22px;
  }
</style>
</head>
<body>
  <main class="letterhead">
    <header>
      <div class="brand">
        <span class="brand-dot"></span>
        <span class="brand-name">North Lark Upkeep Services</span>
      </div>
      <div class="header-rule"></div>
      <address class="contact" style="font-style:normal">
        <div class="contact-address">18 Harbour Row, Elmstead<br>&nbsp;&nbsp;ZIP 4021</div>
        <div class="contact-line">
          <svg viewBox="0 0 10 10"><circle cx="5" cy="5" r="5" fill="var(--brand)"/><path d="M3.2 2.6l1 1-.5.6c.4.8 1 1.4 1.8 1.8l.6-.5 1 1-.7.8C4.9 7.2 2.8 5.1 2.4 3.3z" fill="#fff"/></svg>
          <span>555-014-2100</span>
        </div>
        <div class="contact-line">
          <svg viewBox="0 0 10 10"><circle cx="5" cy="5" r="5" fill="var(--brand)"/><rect x="2.4" y="3.2" width="5.2" height="3.6" fill="#fff"/><path d="M2.4 3.2L5 5.2l2.6-2" stroke="var(--brand)" stroke-width=".6" fill="none"/></svg>
          <span>office@northlarkupkeep.com</span>
        </div>
        <div class="contact-line">
          <svg viewBox="0 0 10 10"><circle cx="5" cy="5" r="5" fill="var(--brand)"/><circle cx="5" cy="5" r="2.6" fill="none" stroke="#fff" stroke-width=".7"/><path d="M2.4 5h5.2M5 2.4c-1.2 1.6-1.2 3.6 0 5.2M5 2.4c1.2 1.6 1.2 3.6 0 5.2" stroke="#fff" stroke-width=".5" fill="none"/></svg>
          <span>www.northlarkupkeep.com</span>
        </div>
      </address>
    </header>

    <section class="letter">
      <h1 class="salutation">Dear Mr. Harlow,</h1>
      <p>Lorem ipsum dolor sit amet, consectetuer adipiscing elit, sed diam nonummy nibh euismod tincidunt ut laoreet dolore magna aliquam erat volutpat. Ut wisi enim ad minim veniam, quis nostrud exerci tation ullamcorper suscipit lobortis nisl ut aliquip ex ea commodo consequat. Duis autem vel eum iriure dolor in hendrerit in vulputate velit esse molestie consequat, vel illum dolore eu feugiat</p>
      <p>Rorem ipsum dolor sit amet, consectetuer adipiscing elit, sed diam nonummy nibh euismod tincidunt ut laoreet dolore magna aliquam erat volutpat. Ut wisi enim ad minim veniam, quis nostrud exerci tation ullamcorper suscipit lobortis nisl ut aliquip ex ea commodo consequat. Duis autem vel eum iriure dolor in hendrerit in vulputate velit esse molest</p>
      <p>Dorem ipsum dolor sit amet, consectetuer adipiscing elit, sed diam nonummy nibh euismod tincidunt ut laoreet dolore magna aliquam erat volutpat. Ut wisi enim ad minim veniam, quis nostrud exerci tation ullamcorper suscipit lobortis nisl ut aliquip ex ea commodo consequat. Duis autem vel eum iriure dolor in hendrerit in suscipit lobortis nisl ut aliquip ex ea commodo consequat. Duis autem vel eum iriure dolor in hendrerit in vulputate velit esse molestie consequat, vel illum</p>
      <p>Sorem ipsum dolor sit amet, consectetuer adipiscing elit, sed diam nonummy nibh euismod tincidunt ut laoreet dolore magna aliquam erat volutpat. Ut wisi enim ad minim veniam, quis nostrud exerci tation ullamcorper suscipit lobortis nisl ut aliquip ex ea commodo consequat. Duis autem vel eum iriure dolor in</p>
      <div class="closing">Sincerely,</div>
      <span class="signature" role="img" aria-label="Handwritten signature of the sender"></span>
    </section>

    <svg class="footer-band" viewBox="0 0 636 22" preserveAspectRatio="none" aria-hidden="true">
      <defs>
        <linearGradient id="bandLeft" x1="0" x2="1" y1="0" y2="0">
          <stop offset="0" stop-color="#00A9DD"/>
          <stop offset=".55" stop-color="#0677BA"/>
          <stop offset="1" stop-color="#1e2a78"/>
        </linearGradient>
        <linearGradient id="bandRight" x1="0" x2="1" y1="0" y2="0">
          <stop offset="0" stop-color="#00A9DD"/>
          <stop offset=".5" stop-color="#0677BA"/>
          <stop offset="1" stop-color="#1e2a78"/>
        </linearGradient>
      </defs>
      <polygon points="0,12 382,12 372,22 0,22" fill="url(#bandLeft)"/>
      <polygon points="390,0 636,0 636,22 378,22 384,12" fill="url(#bandRight)"/>
    </svg>
  </main>
</body>
</html>
```